Spread for a luxury home magazine

- introduce owner and team with headshots and bios
- list benefits of choosing our title company
- luxury/elegant aesthetic

Will send more headshots and bios as things progress

```html
<!DOCTYPE html>
<html lang="en">
<head>
<meta charset="utf-8">
<title>Luxury Elegant Aesthetic – Team Spread</title>
<link href="https://fonts.googleapis.com/css2?family=Open+Sans:wght@400;800&family=Hind:wght@700&family=Lato:wght@400&display=swap" rel="stylesheet">
<style>
:root{
  --backdrop:#e9e9e9;
  --paper:#f3f3f2;
  --paper-shade:#e6e6e5;
  --ink:#1d1d1d;
  --body-ink:#555;
  --rule:#bdbdbd;
  --gold-dark:#b8913a;
  --gold-light:#f3dc8a;
  --gold-mid:#d4ae52;
}
*{margin:0;padding:0;box-sizing:border-box}
html,body{width:1121px;height:1200px;overflow:hidden;background:var(--backdrop)}
.spread{position:absolute;left:0;top:266px;width:1121px;height:667px;
  background:linear-gradient(135deg,var(--paper),#fafafa 40%,var(--paper-shade));
  box-shadow:0 6px 18px rgba(0,0,0,.18)}
.gutter{position:absolute;left:552px;top:0;width:16px;height:667px;
  background:linear-gradient(90deg,transparent,rgba(0,0,0,.08) 50%,transparent)}
.page-art{position:absolute;left:0;top:0;width:560px;height:667px;overflow:hidden}
.page-art svg{position:absolute;left:0;top:0}
.ornament{position:absolute;border-radius:8px;
  background:radial-gradient(ellipse at center,rgba(200,170,100,.22),rgba(120,120,120,.10) 60%,transparent 80%)}
.title-block{position:absolute;left:67px;top:200px;border-left:1px solid var(--ink);padding-left:10px;
  font-family:"Open Sans",sans-serif;color:var(--ink)}
.title-block .t-light{font-size:20px;letter-spacing:2px;line-height:26px;font-weight:400}
.title-block .t-bold{font-size:33px;letter-spacing:2.5px;line-height:36px;font-weight:800}
.title-block .t-light2{font-size:20px;letter-spacing:2px;line-height:28px;font-weight:400}
.team{position:absolute;left:561px;top:0;width:560px;height:667px}
.member{position:absolute;left:0;width:560px}
.headshot{position:absolute;left:36px;width:84px;height:84px;border-radius:50%;
  background:linear-gradient(135deg,var(--gold-dark),var(--gold-light) 50%,var(--gold-mid));padding:4px}
.headshot span{display:block;width:100%;height:100%;border-radius:50%;border:3px solid #fff;
  background:radial-gradient(circle at 50% 40%,#c9a58c,#6b4a3a 70%,#3a2a24)}
.name{position:absolute;left:136px;font-family:"Hind",sans-serif;font-weight:700;font-size:16.5px;color:var(--ink);line-height:18px}
.rule{position:absolute;left:136px;width:391px;height:1px;background:var(--rule)}
.rule::before{content:"";position:absolute;left:0;top:-1px;width:62px;height:3px;
  background:linear-gradient(90deg,var(--gold-dark),var(--gold-light),var(--gold-mid))}
.bio{position:absolute;left:136px;width:391px;font-family:"Lato",sans-serif;font-size:6.1px;line-height:7.9px;color:var(--body-ink);text-align:justify}
.bio p+p{margin-top:7px}
</style>
</head>
<body>
<div class="spread">
  <div class="page-art">
    <div class="ornament" style="left:0;top:0;width:250px;height:130px" role="img" aria-label="Decorative charcoal and gold brush strokes"></div>
    <div class="ornament" style="left:0;top:230px;width:90px;height:100px" role="img" aria-label="Decorative gold brush swash"></div>
    <div class="ornament" style="left:60px;top:520px;width:470px;height:147px" role="img" aria-label="Decorative charcoal and gold brush rings"></div>
    <svg width="560" height="667" viewBox="0 0 560 667">
      <defs>
        <linearGradient id="gold" x1="0" y1="0" x2="1" y2="1">
          <stop offset="0" stop-color="#b8913a"/><stop offset=".5" stop-color="#f3dc8a"/><stop offset="1" stop-color="#c9a24b"/>
        </linearGradient>
        <linearGradient id="room" x1="0" y1="0" x2="0" y2="1">
          <stop offset="0" stop-color="#e4e2e3"/><stop offset=".35" stop-color="#b9a8a3"/>
          <stop offset=".62" stop-color="#8d8a96"/><stop offset=".8" stop-color="#b4531f"/><stop offset="1" stop-color="#e8e6e4"/>
        </linearGradient>
      </defs>
      <polygon role="img" aria-label="Photo of a luxury living room with a grey sofa and orange rug" points="292,53 501,196 501,490 292,632 83,490 83,196" fill="url(#room)"/>
      <polygon points="292,53 501,196 501,490 292,632 83,490 83,196" fill="none" stroke="url(#gold)" stroke-width="4"/>
      <polygon points="153,110 259,185 259,334 153,407 47,334 47,185" fill="#fff" fill-opacity=".82" stroke="url(#gold)" stroke-width="1.5"/>
    </svg>
    <div class="title-block">
      <div class="t-light">LUXURY</div>
      <div class="t-bold">ELEGANT</div>
      <div class="t-light2">AESTHETIC</div>
    </div>
  </div>
  <div class="gutter"></div>

  <div class="team">
    <div class="ornament" style="right:0;top:0;width:115px;height:56px" role="img" aria-label="Decorative gold and charcoal corner accent"></div>

    <div class="member" style="top:0">
      <div class="headshot" style="top:53px" role="img" aria-label="Headshot of Autumn Hale"><span></span></div>
      <div class="name" style="top:50px">Autumn Hale</div>
      <div class="rule" style="top:74px"></div>
      <div class="bio" style="top:84px">
        <p>From the sunny coast of California to the mountainous resort-style lake town of Coeur d'Alene, Idaho to now, the great state of Texas, my passion for providing exceptional service in the real estate industry has been unwavering. As an Escrow Assistant, I bring 4 years of experience in facilitating smooth transactions and ensuring client satisfaction. My escrow experience has allowed me to flourish into the my current role with Keystone Title, where my knowledge of what takes place behind the scenes, always lets me be one step ahead.</p>
        <p>Outside of work, I enjoy being active, traveling and you cannot keep me away from the water. Being an aunt and a faithful Harbor Hawks fan are my two favorite titles, and I can't wait to continue to see what San Antonio sports has to offer.</p>
      </div>
    </div>

    <div class="member" style="top:0">
      <div class="headshot" style="top:169px" role="img" aria-label="Headshot of Tara Lindqvist"><span></span></div>
      <div class="name" style="top:161px">Tara Lindqvist</div>
      <div class="rule" style="top:185px"></div>
      <div class="bio" style="top:195px">
        <p>Recently moving from DFW, I have a hunger to grow my market in South Texas and San Antonio. Building my book of business and providing the best service in SA is my daily driver to get out of my comfort zone and generate new leads that will turn into life-long clients. Going along with that is acceptance of change. I welcome new systems and any industry changes, which I tend to use to my advantage. Working in numerous environments within real estate allows my flexible and adaptable personality to flourish.</p>
        <p>I personally enjoy living an active lifestyle. Whether it's running, hiking, or golfing, you will always find me on the go and looking for the next best version of myself. I am an avid Dallas sports fan; always supporting my Stallions, Pioneers, and Comets.</p>
      </div>
    </div>

    <div class="member" style="top:0">
      <div class="headshot" style="top:294px" role="img" aria-label="Headshot of Grace Moreland"><span></span></div>
      <div class="name" style="top:282px">Grace Moreland</div>
      <div class="rule" style="top:306px"></div>
      <div class="bio" style="top:316px">
        <p>I've been in Real Estate for over 10 years, starting as a marketing assistant for a real estate publication which grew into transaction coordinating and office managing. Those years of experiences allowed me to learn Commercial, Residential and Farm &amp; Ranch transactions like the back of my hand. Always looking toward an opportunity to learn, I decided to venture into an Escrow and apply the transaction coordinating touch to every file while finishing every closing with a special and engaging closing experience. After all, it's not every day you buy or sell a home, and that should be celebrated!</p>
        <p>When I am not in the office creating memorable closing experiences, you can find me on a running or hiking trail with my sweet husband, Doberman, and German Shepherd. I find Zen in cooking and breadmaking, especially to Carb-load before a half marathon race weekend. Saturday nights and Sunday mornings are for Grand Prix racing or watching the Silver Crown saga extended edition again!</p>
      </div>
    </div>

    <div class="member" style="top:0">
      <div class="headshot" style="top:414px" role="img" aria-label="Headshot of Michelle Corbin"><span></span></div>
      <div class="name" style="top:421px">Michelle Corbin</div>
      <div class="rule" style="top:445px"></div>
      <div class="bio" style="top:455px">
        <p>The GIF queen of our office, I am a fun &amp; spunky closer who works with all kinds of agents: from luxury closings to meticulously assisting new agents, from accepted offer to the closing table. When you start off your week with me, you're going to kick off your week on a high note. My energy and caring nature will have your clients leaving our office excited and ready to begin the newest chapter in their life in their new home!</p>
      </div>
    </div>

    <div class="member" style="top:0">
      <div class="headshot" style="top:530px" role="img" aria-label="Headshot of Linda Paxton"><span></span></div>
      <div class="name" style="top:539px">Linda Paxton</div>
      <div class="rule" style="top:563px"></div>
      <div class="bio" style="top:573px">
        <p>I believe that the best thing I can do for my clients is to be kind and warm, as if you were working with a real estate guardian angel. I am always going to look out for you no matter what, just like I do for my family. Having worked as a realtor with Crestline Realty for 13 years and going on 9 years in title, I will leave no stone unturned when it comes to attention to detail. My experience, quality of work and attentiveness to our partners is a commodity that personifies our company's standard to serve your clients and their families. I am also BILINGUAL!</p>
      </div>
    </div>
  </div>
</div>
</body>
</html>
```